Breakthrough Sports Drink Needs a Label Design

Using the logo provided, we need a label design for a new sports drink company called 'Vomra'. We have developed a clear and light, protein-infused beverage for elite athletes.

We would like to label to use a similar color scheme as the logo provided. It needs to portray a refreshing, healthy feel but also needs to reflect the functional aspects of the drink.

The label needs to clearly include the phrases: "18 grams of protein", "For the Elite Athlete" and " "2:1 ratio of carbs to protein "

Target Market(s)

College Athletes

Industry/Entity Type

It Company

Requirements
Must have
• Should be based on the logo provided and include the phrases:
• 18g of Protein
• For The Elite Athlete
• 2:1 Ratio of Carbs to Protein

```html
<!DOCTYPE html>
<html lang="en">
<head>
<meta charset="utf-8">
<title>Vomra Athletic Recovery – Bottle Label</title>
<link href="https://fonts.googleapis.com/css2?family=Open+Sans:wght@600;700;800&display=swap" rel="stylesheet">
<style>
  :root {
    --page-bg: #ffffff;
    --label-bg: #e8ebee;
    --band-light: #dfe9f4;
    --band-blue: #c6dcf1;
    --brand-grey: #5b5e63;
    --accent-blue: #2f8fdc;
    --badge-top: #6fb3ec;
    --badge-bottom: #2f7fd0;
    --badge-rim: #c9ced4;
    --badge-rim-dark: #9aa1a9;
    --ink-dark: #2b2d30;
    --white: #ffffff;
  }
  * { margin: 0; padding: 0; box-sizing: border-box; }
  html, body {
    width: 1200px;
    height: 1000px;
    overflow: hidden;
    background: var(--page-bg);
    font-family: "Open Sans", Arial, sans-serif;
  }
  .label {
    position: absolute;
    left: 300px;
    top: 120px;
    width: 600px;
    height: 760px;
    background: var(--label-bg);
    overflow: hidden;
    box-shadow: 0 2px 10px rgba(0,0,0,0.08);
  }
  .label-bands {
    position: absolute;
    inset: 0;
    width: 100%;
    height: 100%;
  }
  .vertical {
    position: absolute;
    writing-mode: vertical-rl;
    transform: rotate(180deg);
    white-space: nowrap;
  }
  .brand-name {
    left: 62px;
    bottom: 70px;
    font-size: 168px;
    font-weight: 700;
    line-height: 1;
    letter-spacing: 2px;
    color: var(--brand-grey);
  }
  .product-line {
    left: 254px;
    bottom: 78px;
    font-size: 54px;
    font-weight: 700;
    line-height: 1;
    letter-spacing: 1px;
    color: var(--accent-blue);
  }
  .badge {
    position: absolute;
    left: 360px;
    width: 136px;
    height: 200px;
    border-radius: 26px;
    padding: 6px;
    background: linear-gradient(135deg, var(--badge-rim), var(--badge-rim-dark), var(--badge-rim));
  }
  .badge-inner {
    width: 100%;
    height: 100%;
    border-radius: 20px;
    background: linear-gradient(180deg, var(--badge-top), var(--badge-bottom));
    color: var(--white);
    text-align: center;
    display: flex;
    flex-direction: column;
    justify-content: center;
    align-items: center;
  }
  .badge-figure {
    font-size: 66px;
    font-weight: 800;
    line-height: 1;
    margin-bottom: 6px;
  }
  .badge-caption {
    font-size: 17px;
    font-weight: 700;
    line-height: 1.15;
    text-transform: uppercase;
  }
  .badge-ratio { top: 36px; }
  .badge-protein { top: 262px; }
  .tagline {
    position: absolute;
    left: 352px;
    top: 506px;
    width: 152px;
    text-align: center;
    font-size: 17px;
    font-weight: 700;
    line-height: 1.25;
    letter-spacing: 0.5px;
    text-transform: uppercase;
    color: var(--accent-blue);
  }
  .volume {
    position: absolute;
    left: 360px;
    top: 612px;
    width: 136px;
    text-align: center;
    font-size: 34px;
    font-weight: 700;
    line-height: 1.05;
    color: var(--ink-dark);
  }
</style>
</head>
<body>
  <main class="label">
    <svg class="label-bands" viewBox="0 0 600 760" preserveAspectRatio="none" aria-hidden="true">
      <polygon points="0,430 600,150 600,330 0,620" fill="var(--band-light)"/>
      <polygon points="0,560 600,300 600,470 0,730" fill="var(--band-blue)"/>
    </svg>

    <h1 class="vertical brand-name">VOMRA</h1>
    <p class="vertical product-line">ATHLETIC RECOVERY</p>

    <div class="badge badge-ratio">
      <div class="badge-inner">
        <span class="badge-figure">2:1</span>
        <span class="badge-caption">Carbs<br>to<br>Protein</span>
      </div>
    </div>

    <div class="badge badge-protein">
      <div class="badge-inner">
        <span class="badge-figure">18</span>
        <span class="badge-caption">Grams<br>of<br>Protein</span>
      </div>
    </div>

    <p class="tagline">For the<br>Elite Athlete</p>

    <p class="volume">500<br>ML</p>
  </main>
</body>
</html>
```